Health & Nutrition - Business Cards

Needs to look new-age, simple, and elegant. The cards are for my services/counsel in health and nutrition - which include mind, body, and soul. I would like to see something clean and simple but beautiful. Can have a plain background or with a pattern but I don't want it to take away from my contact details. Therefore, my info can be on the back of the card and a nice front design. I really like the flower of life symbol. The name of my business is called Velvet Meadow.

Target Market(s)

Clients - men & women age 20-60. Adults, parents, teachers, sick individuals seeking nutrient counseling and dietary management.

Industry/Entity Type

Nutritionist

Contact Information for Business Card

Tomas Brindle
Cell: 345-827-4602
Email: tbrindle@quillpost.example

Colors
33a6d7
33b8a4
add136
ffffff
5c5c5c
f04a50
fbee3f
cedeed
85cae6

Requirements
Nice to have
• Maybe it can have some sort of sacred geometry as well, but not required. Nice to have the colors that I choose in the project but feel free to come up with your own use of colors. Thanks! =)

```html
<!DOCTYPE html>
<html lang="en">
<head>
<meta charset="utf-8">
<title>Velvet Meadow – Business Cards</title>
<link href="https://fonts.googleapis.com/css2?family=Libre+Baskerville&family=Arimo:wght@400&display=swap" rel="stylesheet">
<style>
  :root {
    --stage: #2b2b2e;
    --card: #1f2224;
    --card-edge: #2a2e30;
    --ink: #ffffff;
    --muted: #c9cccd;
    --accent: #add136;
    --rule: #6b6f71;
  }
  * { margin: 0; padding: 0; box-sizing: border-box; }
  html, body {
    width: 1200px;
    height: 800px;
    overflow: hidden;
    background: var(--stage);
  }
  .canvas {
    width: 1200px;
    height: 800px;
    display: flex;
    align-items: center;
    justify-content: center;
    gap: 48px;
  }
  .card {
    width: 525px;
    height: 300px;
    background: var(--card);
    border: 1px solid var(--card-edge);
    border-radius: 4px;
    position: relative;
    box-shadow: 0 18px 40px rgba(0,0,0,0.35);
  }
  .brand {
    display: flex;
    align-items: center;
    gap: 14px;
    font-family: "Libre Baskerville", serif;
    color: var(--ink);
  }
  .brand-dot {
    width: 34px;
    height: 34px;
    border-radius: 50%;
    background: var(--accent);
    flex: none;
  }
  .card--front .brand {
    position: absolute;
    left: 50%;
    top: 50%;
    transform: translate(-50%, -50%);
    font-size: 30px;
    white-space: nowrap;
  }
  .card--back .brand {
    position: absolute;
    left: 34px;
    top: 180px;
    font-size: 22px;
    white-space: nowrap;
  }
  .card--back .brand-dot { width: 26px; height: 26px; }
  .divider {
    position: absolute;
    left: 262px;
    top: 70px;
    width: 1px;
    height: 150px;
    background: linear-gradient(to bottom, transparent, var(--rule), transparent);
  }
  .contact {
    position: absolute;
    left: 290px;
    top: 78px;
    color: var(--ink);
  }
  .contact-name {
    font-family: "Libre Baskerville", serif;
    font-size: 21px;
    line-height: 1.1;
  }
  .contact-role {
    font-family: "Arimo", sans-serif;
    font-size: 14px;
    color: var(--accent);
    margin-top: 4px;
  }
  .contact-list {
    list-style: none;
    margin-top: 38px;
    font-family: "Arimo", sans-serif;
    font-size: 13px;
    color: var(--muted);
  }
  .contact-list li {
    display: flex;
    align-items: center;
    gap: 8px;
    margin-bottom: 9px;
    white-space: nowrap;
  }
  .contact-icon { width: 16px; height: 16px; flex: none; }
</style>
</head>
<body>
  <main class="canvas">
    <section class="card card--front" aria-label="Card front">
      <div class="brand">
        <span class="brand-dot"></span>
        <span class="brand-name">Velvet Meadow</span>
      </div>
    </section>

    <section class="card card--back" aria-label="Card back">
      <div class="brand">
        <span class="brand-dot"></span>
        <span class="brand-name">Velvet Meadow</span>
      </div>
      <div class="divider"></div>
      <div class="contact">
        <p class="contact-name">Tomas Brindle</p>
        <p class="contact-role">Manager</p>
        <ul class="contact-list">
          <li>
            <svg class="contact-icon" viewBox="0 0 16 16" aria-hidden="true">
              <circle cx="8" cy="8" r="7.2" fill="none" stroke="#add136" stroke-width="1.4"/>
              <rect x="5.6" y="4" width="4.8" height="8" rx="0.8" fill="none" stroke="#add136" stroke-width="1.2"/>
            </svg>
            <span>345-827-4602</span>
          </li>
          <li>
            <svg class="contact-icon" viewBox="0 0 16 16" aria-hidden="true">
              <circle cx="8" cy="8" r="8" fill="#add136"/>
              <rect x="4" y="5.2" width="8" height="5.6" fill="none" stroke="#1f2224" stroke-width="1.1"/>
              <path d="M4 5.4 L8 8.6 L12 5.4" fill="none" stroke="#1f2224" stroke-width="1.1"/>
            </svg>
            <span>tbrindle@quillpost.example</span>
          </li>
        </ul>
      </div>
    </section>
  </main>
</body>
</html>
```